Rack card 4"x9" for a construction company

We need to have a design for:
- the holder of rack cards. Letter size
- and the rack cards. Size 4"x9"

I attached a picture of the sample holder for example.

I am putting some of the brochures and pics we have in:

https://files.quillbarrow.net/folders/7Tz4Qm9WpXc2Lr8VbN3kHs6JdYf0aGeUo?usp=sharing

The Bodoni font is on the drive.
The rack card should call to action - to learn about our projects and that we are offering fixed price packages.

One of the sides of the rack card has to show our houses like we show on the website ferncove-builders.ca
Images with short info like on the website http://www.ferncove-builders.ca/our-projects/
Maybe have something like: Learn more about our recent projects at www...

You can use our logo from th pdf files. In the brochure on the cover page we show all the associations we are member of - this is a must to be shown.

Mentioning the website and the phone number is a must.

Bring your ideas.
Don't hesitate to ask questions.

Thanks
Harold

```html
<!DOCTYPE html>
<html lang="en">
<head>
<meta charset="utf-8">
<title>Ferncove Builders Rack Card</title>
<link href="https://fonts.googleapis.com/css2?family=Bodoni+Moda:wght@500;600&family=Didact+Gothic&family=Montserrat:wght@400;600;700&family=Roboto+Condensed:wght@400&display=swap" rel="stylesheet">
<style>
  :root {
    --navy: #0f1f3d;
    --panel-grey: #e6e6e8;
    --info-grey: #ececee;
    --ink: #141c33;
    --muted: #5a5a5e;
    --white: #ffffff;
    --stage: #7d6a58;
    --sky: #a9dcf0;
    --lawn: #4f8a3a;
  }
  * { box-sizing: border-box; margin: 0; padding: 0; }
  html, body { width: 1200px; height: 1200px; overflow: hidden; }
  body { background: var(--stage); position: relative; font-family: "Didact Gothic", sans-serif; }

  .card { position: absolute; left: 90px; width: 1024px; height: 456px; background: var(--white); box-shadow: 0 4px 14px rgba(0,0,0,.35); }
  .card--front { top: 110px; }
  .card--back { top: 635px; }
  .abs { position: absolute; }

  /* front */
  .intro { left: 21px; top: 22px; width: 311px; height: 368px; background: var(--panel-grey); text-align: center; }
  .brand { margin-top: 70px; display: flex; align-items: center; justify-content: center; gap: 8px; font-family: "Bodoni Moda", serif; font-weight: 600; font-size: 24px; letter-spacing: 1px; color: var(--ink); }
  .brand-mark { width: 12px; height: 12px; background: var(--ink); }
  .headline { margin-top: 38px; font-family: "Bodoni Moda", serif; font-weight: 500; font-size: 38px; line-height: 46px; color: var(--ink); }
  .offer { margin-top: 18px; font-size: 18.5px; line-height: 23px; color: var(--muted); }
  .hero { left: 338px; top: 22px; width: 664px; height: 368px; background: linear-gradient(180deg, var(--sky) 0%, #d7eef6 38%, #8a8f86 55%, #6a7a5c 72%, var(--lawn) 100%); }
  .band { background: var(--navy); color: var(--white); display: flex; align-items: center; justify-content: center; }
  .band--phone { left: 21px; top: 394px; width: 311px; height: 40px; gap: 10px; font-family: "Montserrat", sans-serif; font-weight: 700; font-size: 19px; letter-spacing: .5px; }
  .band--web { left: 338px; top: 394px; width: 664px; height: 40px; font-family: "Montserrat", sans-serif; font-size: 18px; letter-spacing: 3.4px; }

  /* back */
  .story { left: 21px; top: 22px; width: 294px; height: 364px; background: var(--navy); color: var(--white); text-align: center; }
  .story-title { margin-top: 26px; font-family: "Bodoni Moda", serif; font-weight: 500; font-size: 22.5px; line-height: 27px; }
  .story-text { margin: 30px 14px 0; font-size: 15.5px; line-height: 19px; color: #c9ccd6; }
  .story-rule { margin: 22px 18px 0; height: 1px; background: #4a5672; }
  .follow { margin-top: 16px; font-family: "Montserrat", sans-serif; font-weight: 700; font-size: 13px; letter-spacing: 1px; }
  .social { margin-top: 14px; display: flex; justify-content: center; gap: 22px; }
  .social span { width: 20px; height: 20px; border-radius: 50%; background: #c9ccd6; }

  .project { top: 22px; width: 166px; height: 256px; }
  .project-photo { width: 166px; height: 153px; border: 2px solid var(--navy); }
  .project-info { height: 103px; background: var(--info-grey); text-align: center; color: var(--ink); }
  .project-name { padding-top: 12px; font-family: "Bodoni Moda", serif; font-size: 14.5px; line-height: 17px; height: 52px; }
  .specs { display: grid; grid-template-columns: 1.3fr 1fr 1fr; padding: 0 8px; font-family: "Roboto Condensed", sans-serif; font-size: 12.5px; line-height: 19px; }

  .members-title { left: 346px; top: 297px; width: 636px; text-align: center; font-family: "Montserrat", sans-serif; font-weight: 700; font-size: 13.5px; letter-spacing: .5px; color: var(--ink); }
  .members-rule { left: 346px; top: 318px; width: 636px; height: 1px; background: #9a9aa0; }
  .badge { top: 333px; }

  .footer { left: 21px; top: 394px; width: 981px; height: 40px; background: var(--navy); color: var(--white); display: flex; align-items: center; justify-content: space-around; font-family: "Montserrat", sans-serif; font-size: 16px; }
  .footer-item { display: flex; align-items: center; gap: 9px; }
  .footer-item--phone { font-weight: 700; font-size: 19px; }
  .icon-ring { width: 20px; height: 20px; }
</style>
</head>
<body>

<section class="card card--front">
  <div class="abs intro">
    <div class="brand"><span class="brand-mark"></span>FERNCOVE BUILDERS</div>
    <h1 class="headline">Build the home<br>of your dreams</h1>
    <p class="offer">High Quality Custom Houses<br>at Affordable Prices.<br>Fixed price packages available</p>
  </div>
  <div class="abs hero" role="img" aria-label="Rendering of a two-storey craftsman home with stone columns, shingle siding and landscaped front garden"></div>
  <div class="abs band band--phone">
    <svg class="icon-ring" viewBox="0 0 20 20"><circle cx="10" cy="10" r="9" fill="none" stroke="#fff" stroke-width="1.4"/><path d="M6.5 5.5l2 0 .8 2.4-1.2 1a6 6 0 0 0 3 3l1-1.2 2.4.8v2a1 1 0 0 1-1 1A8 8 0 0 1 5.5 6.5a1 1 0 0 1 1-1z" fill="#fff"/></svg>
    604.555.0187
  </div>
  <div class="abs band band--web">www.ferncove-builders.ca</div>
</section>

<section class="card card--back">
  <div class="abs story">
    <h2 class="story-title">Exquisite, Cost-Effective<br>Custom Builds:<br>Your Vision. Your Reality.</h2>
    <p class="story-text">Here is some of our finest work. Each is an example of a vision we turned to reality using only the highest quality building materials. Tremendous craftsmanship takes work. We're happy to oblige.</p>
    <div class="story-rule"></div>
    <div class="follow">FOLLOW US</div>
    <div class="social"><span></span><span></span></div>
  </div>

  <article class="abs project" style="left:323px">
    <div class="project-photo" role="img" aria-label="Three-storey traditional craftsman home with dark trim" style="background:linear-gradient(180deg,#8fc3e6 0%,#c7d3db 40%,#59606a 70%,#4d7a3a 100%)"></div>
    <div class="project-info"><div class="project-name">Renfrew Traditional<br>Craftsman</div>
      <div class="specs"><span>BEDROOMS</span><span>BATH</span><span>SQFT</span><span>7</span><span>5</span><span>3828</span></div></div>
  </article>
  <article class="abs project" style="left:494px">
    <div class="project-photo" role="img" aria-label="Modern craftsman home with stone columns and front garden" style="background:linear-gradient(180deg,#9fd3ec 0%,#c9d6d4 40%,#6f7468 70%,#4f8a3a 100%)"></div>
    <div class="project-info"><div class="project-name">Burnaby Modern<br>Craftsman</div>
      <div class="specs"><span>BEDROOMS</span><span>BATH</span><span>SQFT</span><span>8</span><span>8</span><span>7973</span></div></div>
  </article>
  <article class="abs project" style="left:665px">
    <div class="project-photo" role="img" aria-label="Modern craftsman home lit at dusk" style="background:linear-gradient(180deg,#2b3f86 0%,#5a6598 35%,#b9b6ae 65%,#6d6a64 100%)"></div>
    <div class="project-info"><div class="project-name">Renfrew Modern<br>Craftsman</div>
      <div class="specs"><span>BEDROOMS</span><span>BATH</span><span>SQFT</span><span>9</span><span>7</span><span>4020</span></div></div>
  </article>
  <article class="abs project" style="left:835px">
    <div class="project-photo" role="img" aria-label="Cream-coloured modern luxury home with front stairs at sunset" style="background:linear-gradient(180deg,#c9dbe8 0%,#ede3d2 40%,#d8cdb9 65%,#7a8a62 100%)"></div>
    <div class="project-info"><div class="project-name">Kerrisdale Modern<br>Opulence</div>
      <div class="specs"><span>BEDROOMS</span><span>BATH</span><span>SQFT</span><span>4</span><span>6</span><span>4711</span></div></div>
  </article>

  <div class="abs members-title">PROUD MEMBERS OF</div>
  <div class="abs members-rule"></div>
  <svg class="abs badge" style="left:377px" width="60" height="45" viewBox="0 0 60 45" role="img" aria-label="Association membership badge"><ellipse cx="30" cy="22" rx="28" ry="18" fill="#2a6fb5"/></svg>
  <svg class="abs badge" style="left:503px" width="64" height="45" viewBox="0 0 64 45" role="img" aria-label="Home warranty partner badge"><rect x="12" y="4" width="40" height="37" fill="#c2272d"/></svg>
  <svg class="abs badge" style="left:638px" width="36" height="45" viewBox="0 0 36 45" role="img" aria-label="Builders association member badge"><rect x="2" y="4" width="32" height="37" fill="#1f8a3b"/></svg>
  <svg class="abs badge" style="left:752px" width="56" height="45" viewBox="0 0 56 45" role="img" aria-label="Warranty program badge"><rect x="2" y="6" width="52" height="33" fill="#1e4f8c"/></svg>
  <svg class="abs badge" style="left:878px" width="94" height="45" viewBox="0 0 94 45" role="img" aria-label="Accredited business badge"><rect x="2" y="6" width="90" height="33" rx="4" fill="#1b5fa8"/></svg>

  <div class="abs footer">
    <span class="footer-item footer-item--phone">
      <svg class="icon-ring" viewBox="0 0 20 20"><circle cx="10" cy="10" r="9" fill="none" stroke="#fff" stroke-width="1.4"/><path d="M6.5 5.5l2 0 .8 2.4-1.2 1a6 6 0 0 0 3 3l1-1.2 2.4.8v2a1 1 0 0 1-1 1A8 8 0 0 1 5.5 6.5a1 1 0 0 1 1-1z" fill="#fff"/></svg>
      604.555.0187</span>
    <span class="footer-item">
      <svg class="icon-ring" viewBox="0 0 20 20"><circle cx="10" cy="10" r="9" fill="none" stroke="#fff" stroke-width="1.4"/><rect x="5" y="6.5" width="10" height="7" fill="none" stroke="#fff" stroke-width="1.2"/><path d="M5 6.5l5 4 5-4" fill="none" stroke="#fff" stroke-width="1.2"/></svg>
      contact@ferncove-builders.ca</span>
    <span class="footer-item">
      <svg class="icon-ring" viewBox="0 0 20 20"><circle cx="10" cy="10" r="9" fill="none" stroke="#fff" stroke-width="1.4"/><circle cx="10" cy="10" r="5.5" fill="none" stroke="#fff" stroke-width="1"/><path d="M4.5 10h11M10 4.5c-2.5 3-2.5 8 0 11M10 4.5c2.5 3 2.5 8 0 11" fill="none" stroke="#fff" stroke-width="1"/></svg>
      www.ferncove-builders.ca</span>
  </div>
</section>

</body>
</html>
```